Healthcare Recruitment Agency Brochure

We need our current Brochure updated as its old and dated. The brochure will be for our current and potential Clients and should provide all the necessary information regarding our services, but in a well presented, easy reading format which echoes our company Brand. The company supplies Healthcare establishments with trained healthcare Staff which can be in a variety of settings.
UPDATE: Following the submission of many designs we would like to amend the information/content to be included in the brochure and have uploaded additional information. We would like an 8 page booklet with the various sections spread out so as not to look to 'wordy' page 1 Front cover, 2 About Us, 3 Our Service, 4 Our promise, 5 Our Staff, 6 Our Ethos, 7 What Our Clients Say/Testimonials, 8 Contact Us/Back page. Please if using pictures (which is welcomed) steer away from the surgical/doctor type. We mainly provide care to the Elderly within Nursing and Residential Homes and Support Environments. Thanks

Target Market(s)

Healthcare clientell

Industry/Entity Type

Healthcare

Requirements
Must have
• Pictures, animation, easy reading, informative, tie in with website theme www.silverbrooknursingteam.co.uk
Nice to have
• open to ideas
Should not have
• very long text paragraphs

```html
<!DOCTYPE html>
<html lang="en">
<head>
<meta charset="utf-8">
<title>Silverbrook Nursing Team Brochure</title>
<link href="https://fonts.googleapis.com/css2?family=Rubik:wght@700;800&family=Open+Sans:wght@400;700&display=swap" rel="stylesheet">
<style>
:root{
  --navy:#0f4aa0;
  --deep:#0b3f8f;
  --teal:#0a9b86;
  --ink:#222a33;
  --paper:#f4f5f7;
  --backdrop:#3b3535;
}
*{box-sizing:border-box;margin:0;padding:0}
html,body{width:1200px;height:2423px;overflow:hidden;background:var(--backdrop)}
body{position:relative;font-family:"Open Sans",Arial,sans-serif;color:var(--ink)}
.cover{position:absolute;left:340px;top:30px;width:520px;height:736px;background:var(--paper);overflow:hidden}
.cover-brand{position:absolute;left:34px;top:34px;display:flex;align-items:center;gap:8px;font-weight:700;font-size:19px;color:var(--navy)}
.brand-dot{width:12px;height:12px;border-radius:50%;background:var(--navy)}
.cover-art{position:absolute;left:0;top:0}
.cover-copy{position:absolute;left:34px;bottom:70px;color:#fff}
.cover-title{font-family:"Rubik",Arial,sans-serif;font-weight:800;font-size:34px;line-height:1;letter-spacing:.5px}
.cover-title .accent{display:block;color:var(--teal)}
.cover-sub{margin-top:12px;font-family:"Rubik",Arial,sans-serif;font-weight:700;font-size:16px;line-height:1.3}
.cover-sub .accent{color:#2ec4a8}
.cover-url{position:absolute;right:30px;bottom:26px;color:#fff;font-size:10px}
.page{position:absolute;width:498px;height:705px;background:linear-gradient(180deg,#fbfbfc,#eef0f3);overflow:hidden}
.page-1{left:74px;top:857px}.page-2{left:613px;top:857px}
.page-3{left:74px;top:1622px}.page-4{left:613px;top:1622px}
.page-title{position:absolute;left:50px;top:44px;font-family:"Rubik",Arial,sans-serif;font-weight:800;font-size:28px;color:var(--navy);letter-spacing:.3px}
.page-title .accent{color:var(--teal)}
.page-body{position:absolute;left:48px;right:48px;top:86px}
.lede{font-weight:700;font-size:10.6px;line-height:1.4;margin-bottom:14px}
.points{list-style:none}
.points li{position:relative;padding-left:16px;font-size:8.6px;line-height:1.38;margin-bottom:12px;text-align:justify}
.points li::before{content:"";position:absolute;left:1px;top:3px;width:6px;height:6px;border-radius:50%;border:1.5px solid var(--teal);background:var(--navy)}
.two-col{display:grid;grid-template-columns:1fr 1fr;gap:0 22px}
.two-col .points li{margin-bottom:9px}
.footnote{font-size:8.4px;line-height:1.4;margin-top:4px}
.page-photo{position:absolute;left:0;bottom:0;width:498px;height:330px}
.page-4 .page-photo{height:290px}
</style>
</head>
<body>

<section class="cover">
  <svg class="cover-art" width="520" height="736" viewBox="0 0 520 736">
    <defs>
      <linearGradient id="coverPhoto" x1="0" y1="0" x2="1" y2="1">
        <stop offset="0" stop-color="#e3eef7"/>
        <stop offset="1" stop-color="#8fb0d2"/>
      </linearGradient>
    </defs>
    <rect x="70" y="90" width="420" height="430" rx="20" fill="url(#coverPhoto)" role="img" aria-label="Care assistant supporting a smiling older man in a wheelchair"/>
    <path d="M0 470 C160 440 360 330 520 270 L520 736 L0 736 Z" fill="var(--teal)"/>
    <path d="M0 494 C170 465 360 355 520 296 L520 736 L0 736 Z" fill="var(--deep)"/>
  </svg>
  <div class="cover-brand"><span class="brand-dot"></span>Silverbrook Nursing Team</div>
  <div class="cover-copy">
    <h1 class="cover-title">SUPERIOR<span class="accent">SOLUTIONS</span></h1>
    <p class="cover-sub">We supply qualified,<br><span class="accent">experienced local staff, dedicated</span><br>to delivering excellent services</p>
  </div>
  <div class="cover-url">www.silverbrooknursingteam.co.uk</div>
</section>

<section class="page page-1">
  <h2 class="page-title">ABOUT <span class="accent">US</span></h2>
  <div class="page-body">
    <p class="lede">We know you are busy, but if you could spare a couple of minutes to get to know us a little better, we think you'll really like us;</p>
    <ul class="points">
      <li>Silverbrook Nursing Team is an established and trusted provider of Healthcare Professionals providing flexible temporary Staffing Solutions when its needed most.</li>
      <li>Starting as a small, family run business we have grown with our Clients and now provide support to a vast number of Healthcare Establishments across South East England.</li>
      <li>We can provide Healthcare Assistants, Support Workers and Nurses to cover short and long term assignments on flexible terms to suit your requirements.</li>
      <li>As a CRA accredited company, you can rest assured we will always be working in line with current legislation and guidelines, ensuring best practice.</li>
      <li>We really appreciate our Clients and aim to take the stress out of dealing with agencies by providing a service that excels expectations time and time again.</li>
    </ul>
  </div>
  <svg class="page-photo" viewBox="0 0 498 330">
    <defs><linearGradient id="p1" x1="0" y1="0" x2="1" y2="1"><stop offset="0" stop-color="#e8eef4"/><stop offset="1" stop-color="#4f72a8"/></linearGradient></defs>
    <ellipse cx="249" cy="330" rx="268" ry="222" fill="url(#p1)" role="img" aria-label="Carer sharing a laugh with an older man in a wheelchair"/>
    <ellipse cx="249" cy="330" rx="286" ry="240" fill="none" stroke="var(--navy)" stroke-width="14"/>
    <ellipse cx="249" cy="330" rx="302" ry="256" fill="none" stroke="var(--teal)" stroke-width="12"/>
  </svg>
</section>

<section class="page page-2">
  <h2 class="page-title">OUR <span class="accent">SERVICE</span></h2>
  <div class="page-body">
    <p class="lede">Our Clients often have a lot on their plate which is why we pride ourselves on being extremely accommodating, always putting you first:</p>
    <ul class="points">
      <li>We would welcome the opportunity to speak with you and discuss your Staffing requirements in greater detail should you need support now or in the future.</li>
      <li>Our Client Information Pack contains everything you need to know, including current charge rates, Terms of Business and further information about your Local Branch.</li>
      <li>To begin requesting staff from Silverbrook Nursing Team we simply need a completed Client Account Form which can be signed and returned either via email or post.</li>
      <li>We have staff available to work at the drop of a hat and understand the need for urgency which is why we make it our duty to provide you with continued support.</li>
      <li>Our friendly office staff will always be at the end of the phone to deal with your requests; we never outsource to call centres and operate a 24/7 out of hours service.</li>
    </ul>
  </div>
  <svg class="page-photo" viewBox="0 0 498 330">
    <defs><linearGradient id="p2" x1="0" y1="0" x2="1" y2="1"><stop offset="0" stop-color="#f2f4f6"/><stop offset="1" stop-color="#2f86d6"/></linearGradient></defs>
    <ellipse cx="249" cy="330" rx="268" ry="222" fill="url(#p2)" role="img" aria-label="Nurse in blue scrubs beside an older man in a wheelchair"/>
    <ellipse cx="249" cy="330" rx="286" ry="240" fill="none" stroke="var(--navy)" stroke-width="14"/>
    <ellipse cx="249" cy="330" rx="302" ry="256" fill="none" stroke="var(--teal)" stroke-width="12"/>
  </svg>
</section>

<section class="page page-3">
  <h2 class="page-title">OUR <span class="accent">PROMISE</span></h2>
  <div class="page-body">
    <p class="lede">We work hard to ensure we keep our promises as this creates the foundation for strong and lasting relationships, friendships and business-ships;</p>
    <ul class="points">
      <li>When allocating your requests, we will always try to do so with local, regular Staff who can provide continuity of care to your Residents.</li>
      <li>Once a booking has been placed, we will always keep you updated with our progress whilst being honest and realistic about whether we can assist.</li>
      <li>Compliance forms will be provided for each Staff member booked which details their relevant worker information.</li>
      <li>Staff Rotas will be provided so you can see exactly who is booked to work allowing you to organise your shift allocations.</li>
      <li>We welcome feedback and regularly review our service by sending Staff monitoring forms and arranging review sessions when convenient.</li>
    </ul>
  </div>
  <svg class="page-photo" viewBox="0 0 498 330">
    <defs><linearGradient id="p3" x1="0" y1="0" x2="1" y2="1"><stop offset="0" stop-color="#e6ecf3"/><stop offset="1" stop-color="#2aa9c8"/></linearGradient></defs>
    <ellipse cx="249" cy="330" rx="268" ry="222" fill="url(#p3)" role="img" aria-label="Smiling carer hugging an older woman in a wheelchair"/>
    <ellipse cx="249" cy="330" rx="286" ry="240" fill="none" stroke="var(--navy)" stroke-width="14"/>
    <ellipse cx="249" cy="330" rx="302" ry="256" fill="none" stroke="var(--teal)" stroke-width="12"/>
  </svg>
</section>

<section class="page page-4">
  <h2 class="page-title">OUR <span class="accent">STAFF</span></h2>
  <div class="page-body">
    <p class="lede">We understand the importance for our Clients to have competent, fully trained Staff who can support existing teams which is why all Candidates are subject to the following recruitment and compliance checks;</p>
    <div class="two-col">
      <ul class="points">
        <li>Initial Telephone vetting to ensure suitability for working within Healthcare</li>
        <li>Face-to-face or remote interview including skills and knowledge assessment</li>
        <li>Employment history submitted for the last 10 years with gaps explained</li>
        <li>Right to work documentation has been seen, recorded and verified</li>
        <li>Fitness to work documentation has been declared, assessed and authorised</li>
        <li>Two work related references have been obtained from recent Employers</li>
        <li>An enhanced DBS Certificate has been provided or obtained and verified</li>
      </ul>
      <ul class="points">
        <li>Sufficient training certificates have been provided and verified or;</li>
        <li>In house training courses have been attended and certificates have been issued</li>
        <li>Registration with the appropriate bodies has been verified for Registered Nurses.</li>
        <li>Shadow shift(s) completed for Staff members new to providing Care</li>
        <li>Identification Badge, uniform and timesheets have been issued</li>
        <li>COVID-19 Health Declaration or Immunisation Status received and verified</li>
      </ul>
    </div>
    <p class="footnote">*Our training modules cover all standards set within the Care Certificate and are refreshed on an annual basis*</p>
  </div>
  <svg class="page-photo" viewBox="0 0 498 290">
    <defs><linearGradient id="p4" x1="0" y1="0" x2="1" y2="1"><stop offset="0" stop-color="#9dbb6a"/><stop offset=".6" stop-color="#d9c44a"/><stop offset="1" stop-color="#7a62b8"/></linearGradient></defs>
    <ellipse cx="249" cy="300" rx="268" ry="222" fill="url(#p4)" role="img" aria-label="Carer walking an older man in a wheelchair through a flower garden"/>
    <ellipse cx="249" cy="300" rx="286" ry="240" fill="none" stroke="var(--navy)" stroke-width="14"/>
    <ellipse cx="249" cy="300" rx="302" ry="256" fill="none" stroke="var(--teal)" stroke-width="12"/>
  </svg>
</section>

</body>
</html>
```